Tidemark Book Cover for a new author entering the writing space

Design a stunning, eye catching book cover for a Christian Book. Front, back & spine needs to be designed. I am currently reviewing the final draft so the cover will need to be finalized for print once I have the number of pages and the back cover information.

Book Title: Tidemark
Book Subtitle: Walking steady through the longest season.

Author Name: Dr. Colm Basset

Target Market(s)

Christian readers

Industry/Entity Type

Christian

Colors

Designer to choose colors to be used in the design.

Requirements
Must have
• Bold Title
• Bold Author
• Bold color
• Clean design
Should not have
• No angel wings
• No hands coming out of heaven
• No doves

```html
<!DOCTYPE html>
<html lang="en">
<head>
<meta charset="UTF-8">
<title>Tidemark — Book Cover</title>
<link rel="stylesheet" href="https://fonts.googleapis.com/css2?family=Cinzel:wght@400;600;700&display=swap">
<style>
  :root {
    --page: #ffffff;
    --cover-black: #07040a;
    --cover-top: #120a0c;
    --gold-light: #ffd08a;
    --gold-mid: #e58a2e;
    --gold-deep: #a8430f;
    --text-white: #f4f1f4;
    --nebula-core: #f4d6f2;
    --nebula-violet: #9a5bc2;
    --nebula-red: #a3223a;
    --nebula-blue: #3a2f78;
  }
  * { margin: 0; padding: 0; box-sizing: border-box; }
  html, body {
    width: 1200px;
    height: 900px;
    overflow: hidden;
    background: var(--page);
  }
  .canvas {
    position: relative;
    width: 1200px;
    height: 900px;
    background: var(--page);
  }
  .cover {
    position: absolute;
    left: 298px;
    top: 0;
    width: 635px;
    height: 900px;
    background: var(--cover-black);
    overflow: hidden;
  }
  .cover-header {
    position: absolute;
    left: 0; top: 0;
    width: 100%;
    height: 240px;
    background: radial-gradient(ellipse 60% 70% at 50% 45%, #2a1a16 0%, var(--cover-top) 55%, var(--cover-black) 100%);
  }
  .cover-art {
    position: absolute;
    left: 0;
    top: 240px;
    width: 100%;
    height: 560px;
    background:
      radial-gradient(circle at 52% 48%, var(--nebula-core) 0%, rgba(214,150,220,0.85) 10%, rgba(154,91,194,0.7) 22%, rgba(163,34,58,0.55) 36%, rgba(58,47,120,0.35) 52%, rgba(7,4,10,0) 72%),
      radial-gradient(ellipse 80% 60% at 35% 40%, rgba(163,34,58,0.35) 0%, rgba(7,4,10,0) 70%),
      linear-gradient(180deg, #1a0d14 0%, #140a18 40%, #0d0710 80%, var(--cover-black) 100%);
  }
  .title {
    position: absolute;
    left: 0; top: 78px;
    width: 100%;
    text-align: center;
    font-family: 'Cinzel', serif;
    font-weight: 400;
    font-size: 78px;
    letter-spacing: 6px;
    line-height: 1;
    background: linear-gradient(180deg, var(--gold-light) 0%, var(--gold-mid) 50%, var(--gold-deep) 100%);
    -webkit-background-clip: text;
    background-clip: text;
    color: transparent;
  }
  .subtitle {
    position: absolute;
    left: 0; top: 176px;
    width: 100%;
    text-align: center;
    font-family: 'Cinzel', serif;
    font-weight: 400;
    font-size: 17px;
    letter-spacing: 1.2px;
    color: var(--text-white);
    text-transform: uppercase;
  }
  .author {
    position: absolute;
    left: 0; top: 808px;
    width: 100%;
    text-align: center;
    font-family: 'Cinzel', serif;
    font-weight: 400;
    font-size: 38px;
    letter-spacing: 6px;
    color: var(--text-white);
    text-transform: uppercase;
  }
</style>
</head>
<body>
  <div class="canvas">
    <section class="cover">
      <div class="cover-header"></div>
      <div class="cover-art" role="img" aria-label="Cosmic nebula in violet, red and blue with a glowing geometric emblem at its centre"></div>
      <h1 class="title">TIDEMARK</h1>
      <p class="subtitle">Walking steady through the longest season.</p>
      <p class="author">Dr. Colm Basset</p>
    </section>
  </div>
</body>
</html>
```